***Rustic Website Design - More design needed after!***

Tindlebrook Creative Agency
https://www.picturelane.example/tindlebrookco/

Website pages:
Home
About
Design
-Logo Design and Branding
-Graphic Design
Websites
-Hosting, Maintenance and Support
Social Media
Managed Marketing
Portfolio
Contact

I have included a link to our Picturelane so you get a feel as to how we want to be.

We want to be approachable to new and rural businesses. - Colours included as image

Target Market(s)

Start Up Businesses & Rural Businesses

Number of Pages Required

2 page

Font styles to use
Serif
Other font styles liked:
• Barnyard, Rustic

Requirements
Must have
• Menu, Social Media Icons, rustic lines like our social media.

```html
<!DOCTYPE html>
<html lang="en">
<head>
<meta charset="utf-8">
<title>Tindlebrook Creative Agency</title>
<link href="https://fonts.googleapis.com/css2?family=Libre+Caslon+Text:wght@400;700&family=Nunito:wght@400;600;700;800&display=swap" rel="stylesheet">
<style>
:root{
  --yellow:#f6c418;
  --wood-dark:#2e1a10;
  --wood:#4b2e1d;
  --wood-light:#6a4430;
  --bark:#3a1a10;
  --paper:#ecebe7;
  --paper-shade:#d6d4cf;
  --ink:#2b2523;
  --body:#3b3634;
  --green:#1c5a4d;
  --green-dark:#134438;
  --maroon:#7b2433;
  --night:#151414;
  --white:#ffffff;
  --serif:"Libre Caslon Text", Georgia, serif;
  --sans:"Nunito", Arial, sans-serif;
}
*{margin:0;padding:0;box-sizing:border-box}
html,body{width:1200px;height:4444px;overflow:hidden}
body{position:relative;font-family:var(--sans);color:var(--body);background:var(--paper)}
.section{position:absolute;left:0;width:1200px;overflow:hidden}
.abs{position:absolute}
.btn{position:absolute;display:flex;align-items:center;justify-content:center;background:var(--yellow);color:var(--ink);font:700 13px var(--sans);border-radius:2px;box-shadow:0 2px 4px rgba(0,0,0,.25)}
.heading{font-family:var(--serif);font-weight:400;color:var(--ink);text-align:center;position:absolute;left:0;width:1200px;font-size:40px;letter-spacing:1px}
.wood{background:
  linear-gradient(90deg,rgba(0,0,0,.25),rgba(0,0,0,0) 20%,rgba(0,0,0,.15) 50%,rgba(0,0,0,0) 80%,rgba(0,0,0,.3)),
  linear-gradient(180deg,var(--wood) 0%,var(--wood-light) 45%,var(--wood) 100%)}
.paper{background:radial-gradient(ellipse at 50% 45%,#f4f3f0 0%,var(--paper) 55%,var(--paper-shade) 100%)}

/* header / hero */
.hero{top:0;height:638px}
.hero-curve{position:absolute;top:0;left:0}
.brand{position:absolute;left:69px;top:38px;display:flex;align-items:center;gap:10px;font:700 26px var(--serif);color:var(--white)}
.brand-mark{width:14px;height:14px;background:var(--yellow)}
.nav{position:absolute;left:281px;top:48px;display:flex;gap:28px;font:600 14.5px var(--sans);color:var(--white)}
.nav .active{color:var(--yellow)}
.quote{left:1027px;top:41px;width:101px;height:37px;font-size:13px}
.hero-photo{position:absolute;left:252px;top:126px;width:696px;height:379px;background:linear-gradient(120deg,#cfc6b4 0%,#a8927a 35%,#8b6a4a 60%,#d7c9b0 100%);box-shadow:0 6px 18px rgba(0,0,0,.5)}
.hero-title{position:absolute;left:69px;top:198px;font:700 44px/1.25 var(--serif);color:var(--white)}
.hero-title .hl{color:var(--yellow)}
.hero-sub{position:absolute;left:69px;top:336px;font:400 23px/1.55 var(--sans);color:var(--white)}
.learn{left:70px;top:433px;width:116px;height:36px}
.dots{position:absolute;display:flex;gap:6px}
.dots span{width:10px;height:10px;border-radius:50%;border:1.5px solid var(--yellow)}
.dots span.on{background:var(--yellow)}

/* about */
.about{top:638px;height:577px}
.about-art{position:absolute;left:69px;top:86px;width:551px;height:405px;border-radius:8px;background:radial-gradient(ellipse at 55% 55%,#5e8e8a 0%,#9bb6b8 40%,rgba(236,235,231,0) 72%)}
.about-title{position:absolute;left:668px;top:130px;font:400 40px/1.08 var(--serif);color:var(--ink);letter-spacing:1px}
.about-text{position:absolute;left:669px;top:233px;width:462px;font:400 16px/1.66 var(--sans)}
.about-text p{margin-bottom:14px}
.about .btn{left:670px;top:427px;width:100px;height:35px}

/* services */
.services{top:1215px;height:885px}
.services-intro{position:absolute;left:260px;width:680px;top:155px;text-align:center;font:400 15.5px/1.7 var(--sans)}
.card{position:absolute;width:250px;text-align:center}
.card-frame{position:absolute;left:0;top:0;width:224px;height:183px;border:3px solid var(--green-dark)}
.card-img{position:absolute;left:24px;top:17px;width:226px;height:191px;background:linear-gradient(160deg,#2f6d5f,var(--green-dark));box-shadow:0 3px 8px rgba(0,0,0,.3)}
.card h3{position:absolute;left:0;width:100%;top:234px;font:400 19px var(--serif);color:var(--maroon);letter-spacing:.5px}
.card p{position:absolute;left:0;width:100%;top:268px;font:400 15.5px/1.7 var(--sans);padding:0 4px}
.card .btn{left:78px;top:364px;width:100px;height:35px}

/* portfolio */
.portfolio{top:2100px;height:667px;background:radial-gradient(ellipse at 50% 40%,#f3f1ea 0%,#e7e4dc 60%,#d5d1c7 100%)}
.tile{position:absolute;width:255px}
.portfolio .btn{left:550px;top:591px;width:100px;height:35px}

/* testimonial */
.testimonial{top:2767px;height:509px;background:radial-gradient(ellipse at 50% 40%,#2a6e5f 0%,var(--green) 55%,var(--green-dark) 100%)}
.testimonial .heading{color:var(--white);top:92px}
.heart{position:absolute;border-radius:50% 50% 45% 45%;background:radial-gradient(circle,rgba(246,196,24,.35),rgba(246,196,24,0) 70%)}
.avatar{position:absolute;left:540px;top:170px;width:118px;height:118px;border-radius:50%;border:4px solid var(--yellow);background:radial-gradient(circle at 50% 40%,#c9ddf0,#8fb4d8);box-shadow:0 0 0 3px var(--white) inset}
.qmark{position:absolute;font:700 54px/1 var(--serif);color:var(--white)}
.t-text{position:absolute;left:300px;width:600px;top:309px;text-align:center;font:400 15.5px/1.72 var(--sans);color:var(--white)}
.t-name{position:absolute;left:0;width:1200px;top:389px;text-align:center;font:400 16px var(--sans);color:var(--yellow)}
.t-role{position:absolute;left:0;width:1200px;top:412px;text-align:center;font:400 14px var(--sans);color:var(--white)}

/* feed */
.feed{top:3276px;height:405px}
.feed-tile{position:absolute;top:148px;width:202px;height:174px}

/* contact */
.contact{top:3681px;height:431px}
.contact .heading{color:var(--white);top:50px}
.field{position:absolute;background:var(--white);border-radius:2px;font:700 12.5px var(--sans);color:var(--ink);padding:12px 14px}
.contact .btn{left:550px;top:362px;width:100px;height:36px}

/* footer */
.footer{top:4112px;height:332px;background:var(--night);color:var(--white)}
.socials{position:absolute;left:531px;top:70px;display:flex;gap:6px}
.socials span{width:31px;height:31px;border-radius:50%;background:var(--white)}
.info{position:absolute;top:128px;display:flex;gap:8px;font:400 12px/1.45 var(--sans)}
.info b{font-weight:800;white-space:nowrap}
.footer-nav{position:absolute;left:0;width:1200px;top:205px;display:flex;justify-content:center;gap:26px;font:400 13.5px var(--sans)}
.copy{position:absolute;left:0;width:1200px;top:264px;text-align:center;font:400 12px var(--sans)}
.copy span{color:var(--yellow)}
</style>
</head>
<body>

<section class="section hero wood">
  <svg class="hero-curve" width="1200" height="638" viewBox="0 0 1200 638" aria-hidden="true">
    <path d="M500 0 H1200 V470 C1130 505 1040 510 960 480 C820 430 720 330 640 220 C580 140 530 70 500 0 Z" fill="var(--bark)" opacity=".9"/>
  </svg>
  <div class="brand"><span class="brand-mark"></span>Tindlebrook</div>
  <nav class="nav">
    <span class="active">Home</span><span>About</span><span>Design</span><span>Websites</span><span>Social Media</span><span>Managed Marketing</span><span>Portfolio</span><span>Contact</span>
  </nav>
  <div class="btn quote">Get A Quote</div>
  <div class="hero-photo" role="img" aria-label="Photo of three colleagues reviewing work on a tablet in an office"></div>
  <h1 class="hero-title"><span class="hl">A</span> StartUp<br>Marketing <span class="hl">Agency</span></h1>
  <p class="hero-sub">Long Established Fact That<br>A Reader&nbsp; Distracted</p>
  <div class="btn learn">Learn More</div>
  <div class="dots" style="left:578px;top:548px"><span></span><span class="on"></span><span></span></div>
</section>

<section class="section about paper">
  <div class="about-art" role="img" aria-label="Photo of two open laptops floating in the air"></div>
  <h2 class="about-title">About Tindlebrook<br>Creative Agency</h2>
  <div class="about-text">
    <p>Many desktop publishing packages and web page editors now use Lorem Ipsum as their default model text, and a search for 'lorem ipsum' will uncover .</p>
    <p>Many desktop publishing packages and web page editors now use Lorem Ipsum as their default model text, and a search for 'lorem ipsum' will uncover .</p>
  </div>
  <div class="btn">Read More</div>
</section>

<section class="section services paper">
  <h2 class="heading" style="top:90px">Our Services</h2>
  <p class="services-intro">Many desktop publishing packages and web page editors now use Lorem Ipsum as their default model text, and a search for 'lorem ipsum' will uncover .</p>

  <div class="card" style="left:71px;top:254px">
    <div class="card-frame"></div>
    <div class="card-img" role="img" aria-label="Photo of a keyboard under a green tint with a design icon"></div>
    <h3>Design</h3>
    <p>It is a long established fact that a reader will be distracted by the readable content .</p>
    <div class="btn">Read More</div>
  </div>
  <div class="card" style="left:341px;top:401px">
    <div class="card-frame"></div>
    <div class="card-img" role="img" aria-label="Photo of a laptop under a green tint with a web icon"></div>
    <h3>Websites</h3>
    <p>It is a long established fact that a reader will be distracted by the readable content .</p>
    <div class="btn">Read More</div>
  </div>
  <div class="card" style="left:612px;top:254px">
    <div class="card-frame"></div>
    <div class="card-img" role="img" aria-label="Photo of a gallery wall under a green tint with a network icon"></div>
    <h3>Social Media</h3>
    <p>It is a long established fact that a reader will be distracted by the readable content .</p>
    <div class="btn">Read More</div>
  </div>
  <div class="card" style="left:881px;top:401px">
    <div class="card-frame"></div>
    <div class="card-img" role="img" aria-label="Photo of a workstation under a green tint with a megaphone icon"></div>
    <h3>Managed Marketing</h3>
    <p>It is a long established fact that a reader will be distracted by the readable content .</p>
    <div class="btn">Read More</div>
  </div>
</section>

<section class="section portfolio">
  <svg class="abs" style="left:0;top:0" width="1200" height="14" viewBox="0 0 1200 14" aria-hidden="true">
    <path d="M0 0 H1200 V6 L1140 10 L1080 5 L1000 11 L930 6 L860 12 L780 7 L700 11 L620 5 L540 10 L460 6 L380 12 L300 7 L220 11 L140 5 L60 10 L0 6 Z" fill="var(--paper-shade)"/>
  </svg>
  <h2 class="heading" style="top:57px">Portfolio</h2>
  <div class="tile" role="img" aria-label="Photo of a hand sketching wireframes on a tablet" style="left:71px;top:124px;height:255px;background:linear-gradient(150deg,#d9c8b0,#8f7a66)"></div>
  <div class="tile" role="img" aria-label="Photo of a laptop showing website wireframes next to a coffee cup" style="left:71px;top:395px;height:175px;background:linear-gradient(150deg,#7a5a40,#c9c2b5)"></div>
  <div class="tile" role="img" aria-label="Photo of a branded coffee mug on a wooden table" style="left:338px;top:124px;height:446px;background:linear-gradient(180deg,#5a4a36,#2b2520 55%,#6b5238)"></div>
  <div class="tile" role="img" aria-label="Photo of a digital marketing network diagram" style="left:605px;top:124px;height:255px;background:linear-gradient(160deg,#8a8e93,#4c5156)"></div>
  <div class="tile" role="img" aria-label="Photo of a laptop showing a social media news page" style="left:605px;top:395px;height:175px;background:linear-gradient(160deg,#c9b49a,#6a5646)"></div>
  <div class="tile" role="img" aria-label="Photo of a laptop displaying an image gallery on a desk" style="left:873px;top:124px;height:446px;background:linear-gradient(180deg,#2a2624,#c9c6c2 45%,#e2ddd6)"></div>
  <div class="btn">View All</div>
</section>

<section class="section testimonial">
  <svg class="abs" style="left:0;top:0" width="1200" height="16" viewBox="0 0 1200 16" aria-hidden="true">
    <path d="M0 0 H1200 V8 L1120 12 L1050 6 L970 13 L900 7 L820 12 L740 6 L660 13 L580 8 L500 12 L420 6 L340 13 L260 7 L180 12 L100 6 L0 10 Z" fill="#d5d1c7"/>
  </svg>
  <h2 class="heading">Testimonial</h2>
  <div class="heart" role="img" aria-label="Hand-drawn yellow heart outline" style="left:72px;top:145px;width:156px;height:182px"></div>
  <div class="heart" role="img" aria-label="Small hand-drawn yellow heart outline" style="left:1066px;top:125px;width:64px;height:64px"></div>
  <div class="avatar" role="img" aria-label="Portrait of the client"></div>
  <div class="qmark" style="left:236px;top:282px">&ldquo;</div>
  <div class="qmark" style="left:970px;top:320px">&rdquo;</div>
  <p class="t-text">Many desktop publishing packages and web page editors now use Lorem Ipsum as their default model text, and a search for 'lorem ipsum' will uncover .</p>
  <p class="t-name">- ROWAN ELLERY</p>
  <p class="t-role">Businessman</p>
  <div class="dots" style="left:578px;top:452px"><span></span><span class="on"></span><span></span></div>
</section>

<section class="section feed paper">
  <h2 class="heading" style="top:84px">@The Tindlebrook Creative Agency</h2>
  <div class="feed-tile" role="img" aria-label="Photo of a glowing light bulb" style="left:71px;background:linear-gradient(160deg,#3b2b26,#d88a3a 55%,#2a1f1d)"></div>
  <div class="feed-tile" role="img" aria-label="Photo of hands holding a phone with a shopping app" style="left:285px;background:linear-gradient(160deg,#a37a5a,#e4d8c8)"></div>
  <div class="feed-tile" role="img" aria-label="Photo of devices arranged on a blue desk" style="left:499px;background:linear-gradient(160deg,#3b6e9e,#d98a5a 60%,#2f5a82)"></div>
  <div class="feed-tile" role="img" aria-label="Photo of a phone with social media notifications" style="left:713px;background:linear-gradient(160deg,#2d4f66,#b55a6a 55%,#1f3448)"></div>
  <div class="feed-tile" role="img" aria-label="Photo of hands typing on a laptop beside flowers" style="left:926px;background:linear-gradient(160deg,#e8e6e2,#d87a8a 50%,#5a5654)"></div>
</section>

<section class="section contact wood">
  <h2 class="heading">Contact Us</h2>
  <div class="field" style="left:264px;top:117px;width:221px;height:41px">Name :</div>
  <div class="field" style="left:490px;top:117px;width:221px;height:41px">Email :</div>
  <div class="field" style="left:716px;top:117px;width:220px;height:41px">Phone :</div>
  <div class="field" style="left:264px;top:165px;width:672px;height:185px">Message :</div>
  <div class="btn">Submit</div>
</section>

<footer class="section footer">
  <div class="socials" aria-label="Social links"><span></span><span></span><span></span><span></span></div>
  <div class="info" style="left:160px">
    <svg width="12" height="12" viewBox="0 0 24 24" aria-hidden="true"><path d="M6.6 10.8a15 15 0 0 0 6.6 6.6l2.2-2.2a1 1 0 0 1 1-.25 11.4 11.4 0 0 0 3.6.57 1 1 0 0 1 1 1V20a1 1 0 0 1-1 1A17 17 0 0 1 3 4a1 1 0 0 1 1-1h3.5a1 1 0 0 1 1 1c0 1.25.2 2.450.57 3.57a1 1 0 0 1-.25 1z" fill="var(--yellow)"/></svg>
    <span><b>CALL US :</b>&nbsp; 0400 555 018</span>
  </div>
  <div class="info" style="left:376px">
    <svg width="12" height="15" viewBox="0 0 24 30" aria-hidden="true"><path d="M12 0C5.4 0 0 5.4 0 12c0 9 12 18 12 18s12-9 12-18C24 5.4 18.6 0 12 0zm0 16a4 4 0 1 1 0-8 4 4 0 0 1 0 8z" fill="var(--yellow)"/></svg>
    <b>OUR LOCATION :</b>
    <span style="width:240px;margin-left:12px">Unit 4, Millstone Yard, 12 Hedgerow Lane, Fernbridge, Wessex 30418</span>
  </div>
  <div class="info" style="left:815px">
    <svg width="13" height="10" viewBox="0 0 26 20" aria-hidden="true"><rect width="26" height="20" rx="2" fill="var(--yellow)"/><path d="M1 2l12 9 12-9" stroke="var(--night)" stroke-width="2" fill="none"/></svg>
    <span><b>MAIL US :</b>&nbsp; hello@tindlebrook.example</span>
  </div>
  <nav class="footer-nav">
    <span>Home</span><span>About</span><span>Design</span><span>Websites</span><span>Social Media</span><span>Managed Marketing</span><span>Portfolio</span><span>Contact</span>
  </nav>
  <p class="copy">&copy;Copyright <span>Tindlebrook</span>. All Rights Reserved.</p>
</footer>

</body>
</html>
```